Professional Business Card - TWO SIDES

I need a new business card design to be used by myself and my employees. I would like a professional card and for the front I thought I would like a dark blue thatch with our logo in a raised gold foil on top of it. On the other side I would like name, position, and contact info. I've uploaded our old design for an example of the info used.

Target Market(s)

Business Clients

Industry/Entity Type

CPA Firm

Contact Information for Business Card

Logo, Name, Title, Address, Phone Numbers, Website address, Email Address

Font styles to use
Serif
Sans Serif

Colors
0054AA
0677BA
7BADD7
CADEEF
E8F1F8
0094D4
00A9DD
6FCCEA
C7EBF8
E9F6FB

Requirements
Must have
• Modern Professional Look
Nice to have
• Logo in Gold Foil or ability to have is raised. I like our logo in a single color
Should not have
• I've uploaded old business card

```html
<!DOCTYPE html>
<html lang="en">
<head>
<meta charset="utf-8">
<title>Harlow &amp; Harlow – Business Card</title>
<link rel="stylesheet" href="https://fonts.googleapis.com/css2?family=Oswald:wght@500&family=Arimo:wght@400;700&display=swap">
<style>
  :root {
    --stage: #2b2d31;
    --navy: #15315f;
    --gold: #c99a32;
    --white: #ffffff;
    --ink: #1b2f57;
    --text: #1e1e1e;
  }
  * { box-sizing: border-box; margin: 0; padding: 0; }
  html, body { width: 1200px; height: 900px; overflow: hidden; }
  body {
    background: var(--stage);
    font-family: "Arimo", Arial, sans-serif;
  }
  .canvas {
    position: relative;
    width: 1200px;
    height: 900px;
    display: flex;
    flex-direction: column;
    align-items: center;
    justify-content: center;
    gap: 34px;
  }
  .card {
    position: relative;
    width: 700px;
    height: 400px;
    border-radius: 26px;
    overflow: hidden;
  }
  /* Front */
  .card--front {
    background: var(--navy);
    display: flex;
    flex-direction: column;
    align-items: center;
    justify-content: center;
    color: var(--gold);
  }
  .wordmark {
    font-family: "Oswald", "Arial Narrow", sans-serif;
    font-weight: 500;
    font-size: 72px;
    letter-spacing: 1px;
    line-height: 1;
  }
  .tagline {
    font-family: "Oswald", "Arial Narrow", sans-serif;
    font-weight: 500;
    font-size: 19px;
    letter-spacing: 5px;
    margin-top: 14px;
  }
  /* Back */
  .card--back {
    background: var(--white);
    color: var(--ink);
  }
  .back-brand {
    position: absolute;
    top: 58px;
    left: 0;
    right: 0;
    text-align: center;
    color: var(--ink);
  }
  .back-brand .wordmark { font-size: 58px; }
  .back-brand .tagline { font-size: 15px; letter-spacing: 4px; margin-top: 10px; }
  .person {
    position: absolute;
    top: 212px;
    right: 420px;
    text-align: right;
  }
  .person__name {
    font-weight: 700;
    font-size: 24px;
    color: var(--ink);
    letter-spacing: 0.5px;
  }
  .person__role {
    font-size: 19px;
    color: var(--text);
    margin-top: 4px;
  }
  .divider {
    position: absolute;
    top: 206px;
    left: 296px;
    width: 2px;
    height: 78px;
    background: var(--ink);
  }
  .contacts {
    position: absolute;
    top: 208px;
    left: 316px;
    list-style: none;
    font-size: 18px;
    color: var(--text);
  }
  .contacts li {
    display: flex;
    align-items: center;
    gap: 8px;
    height: 25px;
  }
  .contacts svg { width: 14px; height: 14px; fill: var(--ink); flex: none; }
  .address-band {
    position: absolute;
    left: 0;
    right: 0;
    top: 306px;
    height: 58px;
    background: var(--navy);
    color: var(--white);
    font-size: 19px;
    display: flex;
    align-items: center;
    justify-content: center;
    letter-spacing: 0.3px;
  }
</style>
</head>
<body>
<main class="canvas">
  <section class="card card--front" aria-label="Card front">
    <div class="wordmark">HARLOW &amp; HARLOW</div>
    <div class="tagline">CERTIFIED PUBLIC ACCOUNTANTS</div>
  </section>

  <section class="card card--back" aria-label="Card back">
    <div class="back-brand">
      <div class="wordmark">HARLOW &amp; HARLOW</div>
      <div class="tagline">CERTIFIED PUBLIC ACCOUNTANTS</div>
    </div>

    <div class="person">
      <div class="person__name">DANIEL REYES</div>
      <div class="person__role">Founder</div>
    </div>
    <div class="divider"></div>

    <ul class="contacts">
      <li>
        <svg viewBox="0 0 16 16" aria-hidden="true"><path d="M1 5c0-2 3-3 7-3s7 1 7 3v1h-4V5H5v1H1zM3 7h10l1 7H2z"/></svg>
        (877) 555 0142
      </li>
      <li>
        <svg viewBox="0 0 16 16" aria-hidden="true"><path d="M1 3h14v10H1zM2 4.5v.6l6 4 6-4v-.6l-6 4z"/></svg>
        info@harlowharlow.com
      </li>
      <li>
        <svg viewBox="0 0 16 16" aria-hidden="true"><path d="M8 1a7 7 0 100 14A7 7 0 008 1zm-1 2c-1 1-2 1-2 2s1 1 1 2-1 1-1 2 2 1 2 3-2 0-3-1A5.5 5.5 0 017 3zm3 .5c1 1 0 2 1 3s2 0 2 2-2 1-2 2-1 2-2 2 0-2-1-3 1-2 0-3 1-2 2-3z"/></svg>
        www.harlowharlow.com
      </li>
    </ul>

    <div class="address-band">2140 N. Linden Street Country Name, AB 35870</div>
  </section>
</main>
</body>
</html>
```